American alt-rock band needs eye-catching album cover for new record

We need an album cover for our new cd. The band is called Amber Lantern, the music is alt-rock, an interesting mix of styles and infuences- Elements of The Vanes, K7, Dan Hollis, Walt Brice The Farrows and Carl Whitmoreland are all evident in the sound. Classic rock with atmospheric elements and sweeping melodies. The album is titled "Nothing Stays Where You Left It". We are interested in designs that focus on a single direct subject and are not too busy in nature. Visually striking, yet simple and memorable. Stark contrasts between dark and light. Album covers such as Lumen Drift's "Harbinger", Gray Orchid's "Quiet Edge of The Tide" and Opal Ferry's self titled release are along the lines of what we were hoping for. An idea we had included an image of a man looking at two doors, or two paths, something involving the imagery of decisions (a door number one or number two type concept). Also like simple designs maybe with the subject in a lower corner of the image (this doesn't have to followed if it makes more sense for the image to be centered though). Solid color backgrounds. Colors we like include black, white,deep reds/blues/purples. Not all of them need to be included, but could be (white/black, white/purple, black/red, etc) Please include the band name and album name within the design.

Target Market(s)

18-39

Colors
6b449b
ec1f27
000000
474747
fbfbfb

Requirements
Must have
• Band name and album title must be included in design
Nice to have
• Would like to see something "dream-like" but not too much outer space/sci-fi imagery. Would like to see the moon motel image that I have added used in some way.
Should not have
• no skulls or heavy metal imagery. Dark is ok, but in a more artistic way.

```html
<!DOCTYPE html>
<html lang="en">
<head>
<meta charset="utf-8">
<title>Amber Lantern — Nothing Stays Where You Left It</title>
<link rel="stylesheet" href="https://fonts.googleapis.com/css2?family=Arimo:wght@700&display=swap">
<style>
  :root {
    --ink-white: #fbfbfb;
    --glow-core: #ffffff;
    --glow-magenta: #e21ce0;
    --deep-magenta: #8a0f8c;
    --night-purple: #2a0630;
    --night-black: #000000;
    --shadow-red: #ec1f27;
    --shadow-blue: #3b2fd6;
  }
  html, body {
    margin: 0;
    padding: 0;
    width: 1200px;
    height: 1200px;
    overflow: hidden;
    background: var(--night-black);
  }
  .album-cover {
    position: relative;
    width: 1200px;
    height: 1200px;
    overflow: hidden;
    font-family: "Arimo", Arial, sans-serif;
  }
  .cover-artwork {
    position: absolute;
    inset: 0;
    background:
      radial-gradient(circle at 588px 288px,
        var(--glow-core) 0px,
        #fbd0fb 40px,
        var(--glow-magenta) 150px,
        #c414c8 260px,
        var(--deep-magenta) 520px,
        var(--night-purple) 820px,
        var(--night-black) 1100px);
  }
  .album-title {
    position: absolute;
    left: 86px;
    top: 488px;
    margin: 0;
    font-size: 80px;
    font-weight: 700;
    line-height: 94px;
    letter-spacing: 1px;
    color: var(--ink-white);
    text-shadow:
      -2px -1px 0 var(--shadow-red),
      3px 3px 0 var(--shadow-blue);
  }
  .album-title span {
    display: block;
  }
  .band-name {
    position: absolute;
    left: 92px;
    top: 1052px;
    margin: 0;
    font-size: 36px;
    font-weight: 700;
    letter-spacing: 1.5px;
    word-spacing: 6px;
    color: var(--ink-white);
  }
</style>
</head>
<body>
  <main class="album-cover">
    <div class="cover-artwork" role="img" aria-label="Dreamlike magenta space scene: a bright lens flare with a glowing ring, a small ringed planet at upper left, and a field of halftone dots fading into black"></div>
    <h1 class="album-title">
      <span>Nothing</span>
      <span>Stays</span>
      <span>Where</span>
      <span>You</span>
      <span>Left It</span>
    </h1>
    <p class="band-name">Amber Lantern</p>
  </main>
</body>
</html>
```